Health & Fitness Author & Public Speaker Needs Visually Stunning Web Redesign!

It's time for a redesign of the home page for Verity Halloway's "Bright Fork Kitchen" website (www.brightforkkitchen-example.com). We have a VERY clear idea of what we want, so it really won't take a talented designer long to bring it to life.
The website itself is used to promote & sell her range of health & nutrition programs to a female audience, primarily aged 24 - 35 working in professional or semi professional occupations.
For a VERY comprehensive outline of exactly what we are after, please see the following attached files:
(1) 'Website - WireFrame' (layout, content/copy, visual design style we want along with the desired color scheme)
(2) 'Website - Style Guide' (these are the colours, and overall feel we want)
PLEASE REVIEW THIS IN FULL - THEY WILL GIVE YOU A VERY CLEAR IDEA OF WHAT WE WANT.
Most of the files you need are attached, but for more photos that you can use (of Verity, her programs, and food/meals) can be found at these URL's:
VERITY (profile photos):
https://www.filebinbox.example/sh/qm3rt8wpz1xkd7a/RtPlm4vaNe
ECOVERS
- Bright Fork Kitchen Guide (ebook): https://www.filebinbox.example/sh/wxtnvo5d274ku22/hBqYrsnoz3
- 21 Week Total Momentum Course (ecourse): https://www.filebinbox.example/sh/zopqinr6a2mhwyl/c-dg341oTR
- E-Magazine Issues:
https://www.filebinbox.example/sh/4pzmkar2s9vtyw/57LeWcdDxpB
STOCK IMAGES:
https://www.filebinbox.example/sh/k2qowr8atbnzlx/Qe3HT5mmDy
As we will need to revamp our existing Social page & other printed material, there may be the potential for further work for the successful designer in the future.
Thanks & Good Luck!
Declan Furrow
Marketing & Business Development Manager
Bright Fork Kitchen

```html
<!DOCTYPE html>
<html lang="en">
<head>
<meta charset="utf-8">
<title>Bright Fork Kitchen — Home</title>
<link href="https://fonts.googleapis.com/css2?family=Open+Sans:ital,wght@0,300;0,400;0,600;0,700;1,400&family=Oswald:wght@400;500&family=PT+Sans+Narrow:wght@700&family=Kaushan+Script&display=swap" rel="stylesheet">
<style>
:root{
  --navy:#1f2d42;
  --teal:#36c6bd;
  --pink:#e5225c;
  --ink:#333b45;
  --body:#6a6f76;
  --mist:#f3f3f3;
  --band:#e8e8e8;
  --line:#dcdcdc;
  --white:#ffffff;
}
*{box-sizing:border-box;margin:0;padding:0}
html,body{width:1200px;height:3310px;overflow:hidden}
body{position:relative;background:var(--mist);font-family:"Open Sans",Arial,sans-serif;color:var(--body)}
.abs{position:absolute}

/* header */
.site-header{left:0;top:0;width:1200px;height:110px;background:var(--white)}
.brand{left:124px;top:34px;font-family:"Open Sans",Arial,sans-serif;font-weight:700;font-size:30px;color:var(--pink);display:flex;align-items:center;gap:10px}
.brand-dot{width:16px;height:16px;border-radius:50%;background:var(--pink)}
.main-nav{right:124px;top:64px;display:flex;gap:24px;font-size:14px;font-weight:600;color:var(--ink);text-transform:uppercase}
.main-nav .current{color:var(--pink);border-bottom:3px solid var(--pink);padding-bottom:26px}

/* hero */
.hero{left:0;top:110px;width:1200px;height:456px;background:var(--navy)}
.hero-title{left:124px;top:136px;font-family:"Oswald",sans-serif;font-weight:400;font-size:54px;line-height:62px;color:var(--teal);text-transform:uppercase;letter-spacing:.5px}
.hero-photo{left:800px;top:0;width:290px;height:456px;background:linear-gradient(180deg,#3a3f4d 0%,#6b4f5e 45%,#3a2f45 100%)}

/* signup band */
.signup-band{left:0;top:566px;width:1200px;height:96px;background:var(--pink);color:var(--white)}
.signup-title{left:124px;top:16px;font-size:22px;font-weight:700}
.signup-sub{left:124px;top:50px;font-size:12px;line-height:16px;font-weight:600;width:380px}
.mail-icon{left:514px;top:30px}
.field{height:36px;background:var(--white);border-radius:3px;font-size:13px;color:#9a9a9a;padding:9px 12px}
.signup-band .f1{left:566px;top:30px;width:165px}
.signup-band .f2{left:745px;top:30px;width:165px}
.btn-teal{background:var(--teal);color:var(--white);font-weight:700;border-radius:3px;text-align:center}
.signup-band .go{left:922px;top:30px;width:154px;height:36px;line-height:36px;font-size:15px}

/* press */
.press{left:0;top:662px;width:1200px;height:88px;background:var(--band)}
.press-label{left:124px;top:12px;font-size:13px;font-weight:700;color:var(--ink)}
.press-row{left:124px;top:38px;width:952px;display:flex;justify-content:space-between;align-items:center;font-size:22px;font-weight:700;color:#3a3a3a}

/* content card */
.card{left:97px;top:750px;width:1007px;height:2106px;background:var(--white)}
.main-col{left:21px;top:44px;width:630px}
.lead-title{font-family:"PT Sans Narrow",sans-serif;font-size:27px;line-height:32px;color:var(--pink);margin-bottom:18px}
.copy{font-size:13.5px;line-height:22px;margin-bottom:20px}
.video{position:relative;width:430px;height:248px;background:linear-gradient(160deg,#8fae7a,#c9d6a8 55%,#6d8a5c);margin:34px 0 66px}
.video .play{position:absolute;left:185px;top:94px}
.sec-title{font-family:"PT Sans Narrow",sans-serif;font-size:28px;line-height:34px;color:var(--ink);margin-bottom:18px}
.ticks{list-style:none;margin-bottom:18px}
.ticks li{position:relative;padding-left:30px;font-size:13.5px;line-height:26px}
.ticks li::before{content:"";position:absolute;left:0;top:5px;width:16px;height:16px;border-radius:50%;background:var(--pink)}
.ticks li::after{content:"";position:absolute;left:6px;top:9px;border-left:6px solid var(--white);border-top:4px solid transparent;border-bottom:4px solid transparent}
.ticks.spaced li{font-size:13px;margin-bottom:12px;white-space:nowrap}
.pink-note{font-size:13.5px;color:var(--pink);margin:30px 0 14px}

/* sidebar */
.promo{left:676px;width:303px}
.kick{top:56px;height:266px;border:1px solid var(--line)}
.kick-photo{height:188px;background:linear-gradient(180deg,#b7d99a,#78b06a)}
.kick-foot{height:76px;background:var(--pink);color:var(--white);padding:8px 12px}
.kick-foot b{display:block;font-size:16px;font-weight:700}
.kick-foot span{font-size:10.5px;line-height:13px;display:block}
.order{top:354px;height:300px;border:1px solid var(--line);padding:24px 20px}
.order h3{font-family:"PT Sans Narrow",sans-serif;font-size:28px;color:var(--pink);margin-bottom:14px}
.order p{font-size:12px;line-height:16px;width:140px;color:var(--ink)}
.order .limited{margin-top:18px;color:var(--body)}
.order .buy{display:inline-block;margin-top:14px;padding:6px 14px;font-size:13px}
.cover{left:172px;top:70px;width:110px;height:170px;background:linear-gradient(180deg,#e9e9ea,#c7ccd3)}
.emag{top:665px;height:312px;border:1px solid var(--line);padding:20px 14px}
.emag h3{font-size:15px;font-weight:700;color:#222;text-transform:uppercase}
.mag-stack{width:272px;height:170px;margin:18px 0 20px;background:linear-gradient(90deg,#c8409a,#f07ab0 40%,#6a5fb0 70%,#e14f7c)}
.emag .free{font-family:"PT Sans Narrow",sans-serif;font-size:24px;color:var(--pink);text-align:center}
.social-box{top:1016px;height:265px;border:1px solid var(--line);padding:12px}
.social-head{display:flex;gap:10px;font-size:12px;font-weight:700;color:#3b5a8a}
.social-thumb{width:44px;height:44px;background:#e9c5c5}
.like{display:inline-block;margin-top:4px;font-size:10px;border:1px solid #c0c6d0;padding:1px 6px;color:#555;background:#f2f2f2}
.social-count{font-size:11px;margin:10px 0 8px}
.avatars{display:grid;grid-template-columns:repeat(5,48px);gap:6px 8px;font-size:9px;text-align:center}
.avatars i{display:block;width:48px;height:42px;margin-bottom:2px}
.social-foot{font-size:9.5px;margin-top:10px;color:#888}

/* footer band */
.foot-band{left:0;top:2856px;width:1200px;height:290px;background:var(--band)}
.foot-photo{left:124px;top:-16px;width:138px;height:306px;background:linear-gradient(180deg,#5a3e35,#b9859a 50%,#7a4f8a)}
.foot-title{left:280px;top:40px;font-size:25px;line-height:31px;font-weight:300;color:#555;width:360px}
.foot-sub{left:280px;top:146px;font-size:12px;line-height:16px;font-style:italic;color:var(--pink);width:300px}
.foot-band .mail-icon{left:270px;top:212px}
.foot-band .f1{left:310px;top:214px;width:110px;height:28px;padding:5px 8px;font-size:11px}
.foot-band .f2{left:428px;top:214px;width:110px;height:28px;padding:5px 8px;font-size:11px}
.foot-band .go{left:546px;top:214px;width:110px;height:28px;line-height:28px;font-size:13px}
.help{left:676px;top:14px;font-family:"Kaushan Script",cursive;font-size:17px;color:var(--teal)}
.kick-card{left:676px;top:44px;width:304px;height:166px;background:var(--white);border:1px solid var(--line);padding:18px}
.kick-card b{display:block;font-size:19px;line-height:22px;font-weight:700;color:var(--pink)}
.kick-card em{display:block;font-style:normal;font-size:15px;color:var(--pink);margin-bottom:8px}
.kick-card p{font-size:12px;line-height:16px}

/* footer */
.site-footer{left:0;top:3146px;width:1200px;height:164px;background:var(--pink);color:var(--white)}
.foot-links{left:124px;top:42px;font-size:14px;font-weight:600;display:flex;gap:14px}
.connect{left:880px;top:18px;width:196px;text-align:right;font-size:10px;font-weight:700;letter-spacing:.5px}
.social-dots{left:824px;top:42px;display:flex;gap:14px}
.social-dots span{width:52px;height:52px;border-radius:50%;background:rgba(255,255,255,.85)}
</style>
</head>
<body>

<header class="site-header abs">
  <div class="brand abs"><span class="brand-dot"></span>Bright Fork Kitchen</div>
  <nav class="main-nav abs">
    <span class="current">About Verity</span><span>The Magazine</span><span>Blog &amp; Videos</span><span>Shop</span>
  </nav>
</header>

<section class="hero abs">
  <h1 class="hero-title abs">You don’t need another diet<br>to get the body you want</h1>
  <div class="hero-photo abs" role="img" aria-label="Portrait of Verity seated in a dark top and purple vest"></div>
</section>

<section class="signup-band abs">
  <div class="signup-title abs">Get my FREE monthly E-Magazine</div>
  <div class="signup-sub abs">With delicious recipes,inspirational articles, workouts &amp; expert wellness tips that actually work! Yup FREE!</div>
  <svg class="mail-icon abs" width="36" height="36" viewBox="0 0 36 36"><circle cx="18" cy="18" r="18" fill="#fff"/><rect x="9" y="12" width="18" height="12" fill="none" stroke="#e5225c" stroke-width="2"/><path d="M9 12l9 7 9-7" fill="none" stroke="#e5225c" stroke-width="2"/></svg>
  <div class="field f1 abs">First name</div>
  <div class="field f2 abs">Email</div>
  <div class="btn-teal go abs">Yes Please!</div>
</section>

<section class="press abs">
  <div class="press-label abs">As Seen in:</div>
  <div class="press-row abs">
    <span>Stella Weekly</span><span>Core Motion</span><span>Hearth Notes</span><span>Daybright</span><span>Radiant Woman</span>
  </div>
</section>

<main class="card abs">
  <article class="main-col abs">
    <h2 class="lead-title">Want a Body You’re Proud Of AND a Healthy Lifestyle You Love? Then You Don’t Need Another Diet!</h2>
    <p class="copy">Hey there I’m Verity. I help smart, savvy, driven women just like you to slim down so you can not only rock your outfit but you can enjoy a lifestyle to match. As hard as it might be for you to believe right now, I’ll teach you how to have this in a way that’s easier, and heaps more enjoyable than you’d ever thought possible – it’s time to kiss guilt and deprivation goodbye!</p>
    <div class="video" role="img" aria-label="Video still of Verity sitting on grass in a park">
      <svg class="play" width="60" height="60" viewBox="0 0 60 60"><circle cx="30" cy="30" r="30" fill="rgba(60,60,60,.65)"/><path d="M23 17l20 13-20 13z" fill="#fff"/></svg>
    </div>

    <h2 class="sec-title">Hmmm... do any of these sound familiar?</h2>
    <ul class="ticks">
      <li>Tried a bunch of diet plans but you’re still stuck in a body that just feels yuk</li>
      <li>You “know what to do” but somehow you’re still not doing it (WTF!)</li>
      <li>Suffer from emotional eating, feelings of guilt or frustration around food &amp; exercise</li>
      <li>Feel bloated, guilty and maybe even a bit ashamed</li>
      <li>Overwhelmed and frustrated at yourself, feel that being slim and fit is a never ending chore</li>
    </ul>
    <p class="copy">You’re not the only one… heck that was me at one time. But if you’re exhausted at not liking your body, and sick of seeing other women make it all look so easy, don’t you think maybe it’s time to try something new? Perhaps it’s time you stopped following what everyone else is doing (girlfriends, the 19 year old receptionist at work, or that really buffed chick at the gym)… obviously it’s not working.</p>

    <h2 class="sec-title" style="margin-top:60px">What If I Told You There Was An Easier &amp; More Enjoyable Way?</h2>
    <ul class="ticks">
      <li>To Lose weight (most ladies I work with want to lose between 5kg-10kg… sometimes more)</li>
      <li>Have more energy</li>
      <li>Stop feeling bloated and exhausted</li>
      <li>Stop feeling frustrated for eating the “wrong” things and not exercising “enough”</li>
      <li>Feel hot in your clothes, at work and when you go out</li>
      <li>Feel proud of yourself</li>
      <li>Still have a social life… with you know, friends and stuff!</li>
    </ul>
    <p class="copy">Ok… sounds good so far right, but you’re wondering what is so different from my method? Honestly, the problem with most other diet programs is that they:</p>
    <ul class="ticks spaced">
      <li>Ignore the importance of pleasure in your life for weight loss (I think it’s key)</li>
      <li>Aren’t sustainable – (try and stop me from never eating a French pastry again &amp; see what happens)</li>
      <li>Don’t teach you how to never need to be on another program, plan or diet again.</li>
      <li>Focus on what you need to cut out (I focus on what you need more of in your life to make it more</li>
      <li>pleasurable so you can stop feeding the voids in your life with toxic food, booze, etc)</li>
      <li>Assume you want the same things as everyone else. They assume your definition of healthy should be</li>
      <li>the same as everyone else’s. (I’ll teach you what works for you)</li>
      <li>Ignore the impact that stress has on your ability to shift weight (biochemistry can be cruel).</li>
    </ul>

    <p class="pink-note">I get it. I know and understand first hand your frustrations (I used to be you).</p>
    <h2 class="sec-title">I know you want it to be effortless. I know you want to not worry about putting on weight EVER, you want to just “Be”.</h2>
    <p class="copy">You may have some pieces of the puzzle already, but they just never seem to get together for long enough to get the outcome you truly crave – A hot body you’re proud of with a healthy lifestyle you love. I get it, I understand. And I can help you get there.</p>
    <p class="copy">As a qualified Food &amp; Wellness Coach (and Personal Trainer), I’ve helped thousands of women (as well as myself) just like you over the last 7+ years to not just lose weight (that’s nice) but take back control, regain self confidence and find peace with their bodies (that’s better – trust me). You can do it to.</p>
    <p class="copy">So what now? First things first, sign up for my E-Magazine (it’s FREE!) to receive some really fantastic recipes, inspirational articles, workouts &amp; expert wellness tips each month. You’ll also get sent straight away my Healthy Lifestyle Blueprint to help you get started today!</p>
  </article>

  <aside>
    <div class="promo kick abs">
      <div class="kick-photo" role="img" aria-label="Photo of Verity smiling outdoors among greenery"></div>
      <div class="kick-foot"><b>30 DAY KICK START + DETOX</b><span>A complete step by step program to get you on the path to a hotter, healthier &amp; happier you!</span></div>
    </div>

    <div class="promo order abs">
      <h3>Order Today</h3>
      <p>Yours for the awesome price of just $9.95! (Valued $19.95)</p>
      <p class="limited">*Limited Time Only</p>
      <span class="btn-teal buy">Buy now »</span>
      <div class="cover abs" role="img" aria-label="Cover of the Bright Fork Kitchen Guide ebook"></div>
    </div>

    <div class="promo emag abs">
      <h3>Glow, Fuel, Renew &nbsp;E-Mag</h3>
      <div class="mag-stack" role="img" aria-label="Fanned stack of e-magazine issue covers"></div>
      <div class="free">Your’s FREE Every Month!</div>
    </div>

    <div class="promo social-box abs">
      <div class="social-head"><div class="social-thumb" role="img" aria-label="Page thumbnail"></div><div>Bright Fork Kitchen<br><span class="like">Like</span></div></div>
      <div class="social-count">5,938 likes · 140 talking about this</div>
      <div class="avatars">
        <span><i style="background:#b9a28e"></i>Eva</span><span><i style="background:#8c7a6e"></i>Nora</span><span><i style="background:#c8b3a0"></i>Sonia</span><span><i style="background:#7a8896"></i>Jade</span><span><i style="background:#a3897a"></i>Rhea</span>
        <span><i style="background:#6f7a83"></i>Dan</span><span><i style="background:#c9a8a0"></i>Mara</span><span><i style="background:#d8c2b0"></i>Piper</span><span><i style="background:#9a8f85"></i>Cole</span><span><i style="background:#b09890"></i>Brie</span>
      </div>
      <div class="social-foot">Social plugin</div>
    </div>
  </aside>
</main>

<section class="foot-band abs">
  <div class="foot-photo abs" role="img" aria-label="Standing portrait of Verity in a purple top"></div>
  <h2 class="foot-title abs">Get Slim, Boost Energy, And Create a Healthy Life You Love!</h2>
  <p class="foot-sub abs">Subscribe to my FREE monthly e-magazine for heaps of awesome recipes, workouts &amp; advice!</p>
  <svg class="mail-icon abs" width="32" height="32" viewBox="0 0 36 36"><circle cx="18" cy="18" r="18" fill="#e5225c"/><rect x="9" y="12" width="18" height="12" fill="none" stroke="#fff" stroke-width="2"/><path d="M9 12l9 7 9-7" fill="none" stroke="#fff" stroke-width="2"/></svg>
  <div class="field f1 abs">First name</div>
  <div class="field f2 abs">Email</div>
  <div class="btn-teal go abs">SIGN ME UP!</div>
  <div class="help abs">need a hand getting started?</div>
  <div class="kick-card abs">
    <b>ULTIMATE 30 DAY</b><em>KICK START PROGRAM</em>
    <p>Finally an easy to follow program to help you get slim &amp; eat well, but also help you create a Healthy Life you love!</p>
  </div>
</section>

<footer class="site-footer abs">
  <nav class="foot-links abs"><span>PRIVACY POLICY</span><span>|</span><span>RETURNS &amp; REFUNDS</span><span>|</span><span>CONTACT</span></nav>
  <div class="connect abs">CONNECT WITH VERITY</div>
  <div class="social-dots abs"><span></span><span></span><span></span><span></span></div>
</footer>

</body>
</html>
```